Tellwire Ads Creative In 3 Different Sizes For Marketing Agency

We need a set of ads designed that will be used to run ads for lead generation on tellwire and QV Newsfeed.
So we need the news feed for TW and QV image size and a Carousel Ad size for a total of 3 sizes of same design.
Please reference these links for specs for files:
https://www.tellwire.example/business/ads-guide/carousel
https://www.tellwire.example/business/ads-guide/image
https://www.tellwire.example/business/ads-guide/image/quorvia-feed
Content on ad:
HEADLINE; 2x-5x YOUR SALES & LEADS OVERNIGHT
SUBHEADLINE: OFFER COMPLIMENTARY HOTEL STAYS & $100 DINING CARDS AS A BONUS FOR BUYING YOUR PRODUCT OR SERVICE
(without having to personally fulfill or pay for them yourself!)
Target Market(s)
business owners
Industry/Entity Type
digital marketing agency
Colors
Designer to choose colors to be used in the design.
Requirements
Must have
- Must use my website theme. Feel free to steal images from my website and use them. @ www.zestlanebonuses.example I have included an example of what someone else designed for me as inspiration that I kind of like but im looking for something way better too so please do not copy this one.
Nice to have
- Want to keep theme of website so when they click it and go to my website they kknow they are in the right place so everything is consistent
Should not have
- should not use stock images only use images from my website @ www.zestlanebonuses.example

```html
<!DOCTYPE html>
<html lang="en">
<head>
<meta charset="utf-8">
<title>Zestlane Bonuses – Ad Set in Three Sizes</title>
<link rel="stylesheet" href="https://fonts.googleapis.com/css2?family=Montserrat:wght@800&family=Roboto+Condensed:wght@600&family=Poppins:wght@500&family=Roboto:wght@400;500;700&display=swap">
<style>
:root{
  --page:#e8e8e8;
  --ink:#1a1a1a;
  --purple-deep:#24176e;
  --purple:#3a2a9c;
  --white:#ffffff;
  --green:#8dc63f;
  --line-green:#3ccf3a;
  --blue:#3b7bd8;
  --orange:#d98a4a;
}
*{margin:0;padding:0;box-sizing:border-box}
html,body{width:1200px;height:1025px;overflow:hidden;background:var(--page)}
.canvas{position:relative;width:1200px;height:1025px}
.size-label{position:absolute;font:400 24px/1 "Roboto",sans-serif;color:var(--ink);letter-spacing:1px;transform:translateX(-50%)}
.ad{position:absolute;overflow:hidden;background:var(--purple-deep)}
.ad-photo{position:absolute;inset:0;background:
  radial-gradient(ellipse at 20% 30%,rgba(120,100,200,.55),transparent 60%),
  radial-gradient(ellipse at 80% 60%,rgba(90,75,176,.45),transparent 55%),
  linear-gradient(180deg,#3a2a9c 0%,#2e2186 55%,#24176e 100%)}
.headline,.subline,.fine,.url{position:absolute;white-space:nowrap}
.headline{font-family:"Montserrat",sans-serif;font-weight:800;color:var(--white);line-height:1}
.headline.accent{color:var(--green)}
.subline{font-family:"Roboto Condensed",sans-serif;font-weight:600;color:var(--white);line-height:1}
.fine{font-family:"Poppins",sans-serif;font-weight:500;color:var(--green);line-height:1}
.url{font-family:"Roboto",sans-serif;font-weight:500;color:var(--white);line-height:1}
.url b{color:var(--green);font-weight:700}
.center{left:50%;transform:translateX(-50%)}
.chart{position:absolute;left:0;top:0}
.bonus-visual{position:absolute;border-radius:50%;background:radial-gradient(circle at 55% 50%,rgba(217,138,74,.9) 0%,rgba(160,100,80,.6) 35%,rgba(59,123,216,.35) 60%,rgba(111,210,58,.15) 75%,transparent 100%)}
.brand{position:absolute;display:flex;align-items:center;gap:6px;font-family:"Montserrat",sans-serif;font-weight:800;color:var(--blue);white-space:nowrap;line-height:1}
.brand-mark{background:var(--blue);display:block}
</style>
</head>
<body>
<div class="canvas">

  <div class="size-label" style="left:338px;top:30px">1080 X 1080</div>
  <section class="ad ad-square" style="left:110px;top:64px;width:457px;height:457px">
    <div class="ad-photo" role="img" aria-label="Team of business people gathered around a table, tinted purple"></div>
    <div class="headline center" style="top:22px;font-size:31px">2x-5x YOUR SALES</div>
    <div class="headline accent center" style="top:51px;font-size:20px">&amp; LEADS OVERNIGHT</div>
    <div class="subline center" style="top:85px;font-size:15px">OFFER COMPLIMENTARY HOTEL STAYS &amp; $100 DINING CARDS</div>
    <div class="subline center" style="top:104px;font-size:15px">AS A BONUS FOR BUYING YOUR PRODUCT OR SERVICE</div>
    <div class="fine center" style="top:122px;font-size:13px">(that you don't personally need to fulfill or pay for!)</div>
    <div class="bonus-visual" role="img" aria-label="Circular arrow around fanned hotel and dining gift certificates with airfare voucher" style="left:122px;top:154px;width:212px;height:196px"></div>
    <svg class="chart" width="457" height="457" viewBox="0 0 457 457">
      <polyline points="0,392 10,393 79,400 146,374 217,370 285,361 350,384 423,363 457,355" fill="none" stroke="var(--line-green)" stroke-width="2"/>
      <g fill="#fff" stroke="var(--line-green)" stroke-width="2"><circle cx="10" cy="393" r="5"/><circle cx="79" cy="400" r="5"/><circle cx="146" cy="374" r="5"/><circle cx="217" cy="370" r="5"/><circle cx="285" cy="361" r="5"/><circle cx="350" cy="384" r="5"/><circle cx="423" cy="363" r="5"/></g>
    </svg>
    <div class="brand center" style="top:394px;font-size:13px"><span class="brand-mark" style="width:14px;height:14px"></span>ZESTLANE BONUSES</div>
    <div class="url center" style="top:424px;font-size:14px">www.<b>zestlanebonuses</b>.example</div>
  </section>

  <div class="size-label" style="left:877px;top:471px">400 X 500</div>
  <section class="ad ad-carousel" style="left:612px;top:64px;width:478px;height:383px">
    <div class="ad-photo" role="img" aria-label="Team of business people gathered around a table, tinted purple"></div>
    <div class="headline center" style="top:25px;font-size:29.5px">2x-5x YOUR SALES</div>
    <div class="headline accent center" style="top:54px;font-size:20px">&amp; LEADS OVERNIGHT</div>
    <div class="subline center" style="top:83px;font-size:14px">OFFER COMPLIMENTARY HOTEL STAYS &amp; $100 DINING CARDS</div>
    <div class="subline center" style="top:102px;font-size:14px">AS A BONUS FOR BUYING YOUR PRODUCT OR SERVICE</div>
    <div class="fine center" style="top:120px;font-size:12.5px">(that you don't personally need to fulfill or pay for!)</div>
    <div class="bonus-visual" role="img" aria-label="Circular arrow around fanned hotel and dining gift certificates with airfare voucher" style="left:160px;top:150px;width:172px;height:152px"></div>
    <svg class="chart" width="478" height="383" viewBox="0 0 478 383">
      <polyline points="0,345 48,336 112,340 175,316 241,312 304,304 366,324 433,305 478,296" fill="none" stroke="var(--line-green)" stroke-width="2"/>
      <g fill="#fff" stroke="var(--line-green)" stroke-width="2"><circle cx="48" cy="336" r="5"/><circle cx="112" cy="340" r="5"/><circle cx="175" cy="316" r="5"/><circle cx="241" cy="312" r="5"/><circle cx="304" cy="304" r="5"/><circle cx="366" cy="324" r="5"/><circle cx="433" cy="305" r="5"/></g>
    </svg>
    <div class="brand center" style="top:337px;font-size:11px"><span class="brand-mark" style="width:12px;height:12px"></span>ZESTLANE BONUSES</div>
    <div class="url center" style="top:358px;font-size:12.5px">www.<b>zestlanebonuses</b>.example</div>
  </section>

  <div class="size-label" style="left:608px;top:972px">1200 X 628</div>
  <section class="ad ad-landscape" style="left:224px;top:560px;width:767px;height:402px">
    <div class="ad-photo" role="img" aria-label="Team of business people collaborating, tinted purple"></div>
    <div class="headline" style="left:44px;top:56px;font-size:40px">2x-5x YOUR SALES</div>
    <div class="headline accent" style="left:44px;top:99px;font-size:32px">&amp; LEADS OVERNIGHT</div>
    <div class="subline" style="left:44px;top:159px;font-size:23px">OFFER COMPLIMENTARY HOTEL STAYS &amp;</div>
    <div class="subline" style="left:44px;top:189px;font-size:23px">$100 DINING CARDS AS A BONUS FOR</div>
    <div class="subline" style="left:44px;top:218px;font-size:23px">BUYING YOUR PRODUCT OR SERVICE</div>
    <div class="fine" style="left:44px;top:250px;font-size:16.5px">(that you don't personally need to fulfill or pay for!)</div>
    <div class="bonus-visual" role="img" aria-label="Circular arrow around fanned hotel and dining gift certificates with airfare voucher" style="left:448px;top:30px;width:280px;height:256px"></div>
    <svg class="chart" width="767" height="402" viewBox="0 0 767 402">
      <polyline points="0,355 80,364 189,322 303,315 412,300 519,337 635,302 750,279 767,277" fill="none" stroke="var(--line-green)" stroke-width="2.5"/>
      <g fill="#fff" stroke="var(--line-green)" stroke-width="2.5"><circle cx="80" cy="364" r="7"/><circle cx="189" cy="322" r="7"/><circle cx="303" cy="315" r="7"/><circle cx="412" cy="300" r="7"/><circle cx="519" cy="337" r="7"/><circle cx="635" cy="302" r="7"/><circle cx="750" cy="279" r="7"/></g>
    </svg>
    <div class="url" style="left:141px;top:358px;font-size:18px">www.<b>zestlanebonuses</b>.example</div>
    <div class="brand" style="left:492px;top:356px;font-size:14px"><span class="brand-mark" style="width:18px;height:18px"></span>ZESTLANE BONUSES</div>
  </section>

</div>
</body>
</html>
```